Dutch psychology podcast needs logo / art design

I need a logo / artwork for my new podcast on psychology/health called 'Het Heldere Kwartier'. In the podcast I talk to different experts on subjects as personal development, psychology, health, spirituality and entrepreneurship. I would like to see my brand colors back in the design (www.joramveldkuijl.nl) and my face in the artwork since I'm the host of the show.

My photo is included in the attachments and I've also added some examples of what I'm looking for.

Industry/Entity Type

Psychology

Colors

Designer to choose colors to be used in the design.

Requirements
Must have
• - Name of the show: 'Het Heldere Kwartier' (I prefer that this name is turned into a logo), see attachment of example of Harbor of Wonder
• - Subtitle: 'met Joram Veldkuijl' which is my name a the host
• - My picture, see attachments

```html
<!DOCTYPE html>
<html lang="nl">
<head>
<meta charset="utf-8">
<title>Het Heldere Kwartier – met Joram Veldkuijl</title>
<link href="https://fonts.googleapis.com/css2?family=Roboto+Condensed:wght@700;900&display=swap" rel="stylesheet">
<style>
  :root {
    --teal-deep: #05393b;
    --teal-mid: #0e6e6d;
    --teal-glow: #34d0c6;
    --star: rgba(190, 255, 250, 0.85);
    --star-soft: rgba(150, 240, 232, 0.55);
    --white: #ffffff;
    --signal-red: #e4141b;
    --shirt-navy: #141725;
    --shirt-navy-light: #2a2e40;
  }
  * { margin: 0; padding: 0; box-sizing: border-box; }
  html, body {
    width: 1200px;
    height: 1200px;
    overflow: hidden;
    background: var(--teal-deep);
  }
  .cover {
    position: relative;
    width: 1200px;
    height: 1200px;
    overflow: hidden;
    font-family: "Roboto Condensed", "Arial Narrow", sans-serif;
    color: var(--white);
  }
  .space-backdrop {
    position: absolute;
    inset: 0;
    background:
      radial-gradient(circle at 20% 30%, var(--star) 0 1.2px, transparent 1.8px) 0 0 / 53px 47px,
      radial-gradient(circle at 60% 70%, var(--star-soft) 0 1px, transparent 1.6px) 11px 23px / 37px 41px,
      radial-gradient(circle at 40% 50%, var(--star) 0 1.6px, transparent 2.4px) 29px 7px / 131px 113px,
      radial-gradient(circle at 50% 50%, rgba(220,255,252,0.9) 0 2.4px, transparent 4px) 67px 41px / 263px 229px,
      radial-gradient(ellipse 40% 30% at 28% 72%, rgba(52,208,198,0.6), transparent 70%),
      radial-gradient(ellipse 35% 30% at 72% 48%, rgba(52,208,198,0.5), transparent 70%),
      radial-gradient(ellipse 50% 35% at 15% 15%, rgba(14,110,109,0.7), transparent 75%),
      linear-gradient(160deg, var(--teal-mid) 0%, var(--teal-deep) 50%, var(--teal-mid) 100%);
  }
  .host-portrait {
    position: absolute;
    left: 490px;
    top: 116px;
    width: 710px;
    height: 1084px;
    border-radius: 340px 340px 0 0 / 300px 300px 0 0;
    background:
      radial-gradient(ellipse 22% 26% at 52% 22%, rgba(196,150,128,0.55), transparent 75%),
      linear-gradient(180deg, var(--shirt-navy-light) 0%, var(--shirt-navy) 55%, #0f1220 100%);
  }
  .show-logo {
    position: absolute;
    left: 84px;
    top: 180px;
    display: flex;
    align-items: center;
    gap: 16px;
  }
  .show-logo__name {
    font-weight: 700;
    font-size: 58px;
    line-height: 1;
    text-transform: uppercase;
  }
  .show-logo__dot {
    width: 32px;
    height: 32px;
    border-radius: 50%;
    background: var(--signal-red);
  }
  .host-credit {
    position: absolute;
    left: 114px;
    top: 440px;
    font-weight: 900;
    text-transform: uppercase;
    line-height: 1;
  }
  .host-credit__prefix {
    display: block;
    font-size: 256px;
    letter-spacing: -4px;
    line-height: 0.86;
    margin-left: -4px;
  }
  .host-credit__name {
    display: block;
    font-size: 140px;
    letter-spacing: 0;
    line-height: 0.74;
    margin-top: 30px;
  }
</style>
</head>
<body>
  <main class="cover">
    <div class="space-backdrop" role="img" aria-label="Turquoise starry nebula in deep space"></div>
    <div class="host-portrait" role="img" aria-label="Photo of the host, smiling with arms crossed, wearing a dark navy sweater"></div>

    <div class="show-logo">
      <span class="show-logo__name">Het Heldere Kwartier</span>
      <span class="show-logo__dot"></span>
    </div>

    <h1 class="host-credit">
      <span class="host-credit__prefix">Met</span>
      <span class="host-credit__name">Joram</span>
      <span class="host-credit__name">Veldkuijl</span>
    </h1>
  </main>
</body>
</html>
```